Startup company business card (Media & Advertising)

we need a business card design for a company that is a startup in the media and aggregation industry. Card needs to look funky and of a new breed/modern and upmarket.

Target Market(s)

advertisers/ brand agencies & media publishers

Industry/Entity Type

Advertising

Contact Information for Business Card

Please ensure the front face signifies our brand (plumvexo.com) and back has details for the contact. Standard contact such as phone , address, email , website etc.

Font styles to use
Other font styles liked:
• use styleguide and logo font and color

Colors

Designer to choose colors to be used in the design.

Requirements
Must have
• We are disrupting the media and agency industry so subtlety would be good to use imagery to signify this
Nice to have
• Please use logo colors for branding
Should not have
• be as creative and provide few options. Pick a brand color from logo and styleguide

```html
<!DOCTYPE html>
<html lang="en">
<head>
<meta charset="utf-8">
<title>plumvexo business card</title>
<link rel="stylesheet" href="https://fonts.googleapis.com/css2?family=Montserrat:wght@400;500;600;700&display=swap">
<style>
  :root {
    --backdrop: #3a3d42;
    --card: #060608;
    --brand-red: #ee3a45;
    --brand-red-deep: #a81f42;
    --ink-light: #ffffff;
    --ink-soft: #e6e6e8;
  }
  * { box-sizing: border-box; margin: 0; padding: 0; }
  html, body {
    width: 1200px;
    height: 1000px;
    overflow: hidden;
    background: var(--backdrop);
    font-family: "Montserrat", sans-serif;
  }
  .sheet {
    position: relative;
    width: 1200px;
    height: 1000px;
  }
  .card {
    position: absolute;
    left: 220px;
    width: 760px;
    height: 430px;
    background: var(--card);
    border-radius: 22px;
    overflow: hidden;
  }
  .card--front { top: 45px; }
  .card--back { top: 525px; }

  .brand {
    display: flex;
    align-items: center;
    gap: 20px;
  }
  .brand__mark {
    width: 62px;
    height: 62px;
    border-radius: 50%;
    background: var(--brand-red);
  }
  .brand__name {
    color: var(--ink-light);
    font-weight: 700;
    font-size: 68px;
    letter-spacing: 1px;
    line-height: 1;
  }
  .card--front .brand {
    position: absolute;
    top: 50%;
    left: 50%;
    transform: translate(-50%, -50%);
  }
  .card--back .brand {
    position: absolute;
    top: 48px;
    left: 50%;
    transform: translateX(-50%);
  }
  .card--back .brand__mark { width: 52px; height: 52px; }
  .card--back .brand__name { font-size: 58px; }

  .details {
    position: absolute;
    top: 172px;
    left: 0;
    right: 0;
    display: flex;
    justify-content: center;
    align-items: stretch;
  }
  .person {
    text-align: right;
    padding-right: 22px;
    padding-top: 6px;
  }
  .person__name {
    color: var(--brand-red);
    font-weight: 700;
    font-size: 26px;
    letter-spacing: 3px;
    text-transform: uppercase;
  }
  .person__role {
    color: var(--ink-soft);
    font-weight: 500;
    font-size: 19px;
    margin-top: 4px;
    letter-spacing: 0.5px;
  }
  .divider {
    width: 2px;
    background: var(--ink-soft);
  }
  .contacts {
    list-style: none;
    padding-left: 22px;
    display: flex;
    flex-direction: column;
    gap: 8px;
  }
  .contacts__item {
    display: flex;
    align-items: center;
    gap: 12px;
    color: var(--ink-light);
    font-weight: 500;
    font-size: 19px;
    letter-spacing: 0.8px;
  }
  .contacts__icon {
    width: 18px;
    height: 18px;
    flex: none;
  }
  .address-band {
    position: absolute;
    left: 0;
    right: 0;
    bottom: 34px;
    height: 52px;
    background: linear-gradient(90deg, var(--brand-red), var(--brand-red-deep));
    display: flex;
    align-items: center;
    justify-content: center;
    color: var(--ink-light);
    font-weight: 500;
    font-size: 20px;
    letter-spacing: 1px;
  }
</style>
</head>
<body>
<main class="sheet">
  <section class="card card--front" aria-label="Card front">
    <div class="brand">
      <span class="brand__mark" aria-hidden="true"></span>
      <span class="brand__name">plumvexo</span>
    </div>
  </section>

  <section class="card card--back" aria-label="Card back">
    <div class="brand">
      <span class="brand__mark" aria-hidden="true"></span>
      <span class="brand__name">plumvexo</span>
    </div>

    <div class="details">
      <div class="person">
        <p class="person__name">Marek Elling</p>
        <p class="person__role">General Manager</p>
      </div>
      <span class="divider" aria-hidden="true"></span>
      <ul class="contacts">
        <li class="contacts__item">
          <svg class="contacts__icon" viewBox="0 0 24 24" aria-hidden="true"><path fill="#ee3a45" d="M6.6 10.8a15.2 15.2 0 0 0 6.6 6.6l2.2-2.2a1 1 0 0 1 1-.25 11.4 11.4 0 0 0 3.6.57 1 1 0 0 1 1 1V20a1 1 0 0 1-1 1A17 17 0 0 1 3 4a1 1 0 0 1 1-1h3.5a1 1 0 0 1 1 1c0 1.25.2 2.46.57 3.6a1 1 0 0 1-.25 1z"/></svg>
          844-555-0182
        </li>
        <li class="contacts__item">
          <svg class="contacts__icon" viewBox="0 0 24 24" aria-hidden="true"><rect x="2" y="5" width="20" height="14" rx="1.5" fill="#ee3a45"/><path d="M3 6l9 7 9-7" fill="none" stroke="#060608" stroke-width="1.8"/></svg>
          info@plumvexo.com
        </li>
        <li class="contacts__item">
          <svg class="contacts__icon" viewBox="0 0 24 24" aria-hidden="true"><g fill="none" stroke="#ee3a45" stroke-width="1.8"><circle cx="12" cy="12" r="9.5"/><ellipse cx="12" cy="12" rx="4.2" ry="9.5"/><path d="M2.5 12h19M4 7h16M4 17h16"/></g></svg>
          www.plumvexo.com
        </li>
      </ul>
    </div>

    <p class="address-band">1450 W Harlow Ave Dalton County 70412</p>
  </section>
</main>
</body>
</html>
```